HELP! TALENTED DESIGNERS ONLY! Shipping Box Design for Electronic Trade-in Company!

Our company buys smartphones, tablets, Korvanettes, and a few other select electronics. When a customer wants to sell us a phone, tablet, or laptop and doesn't have a box or packing material to send it in we send them a box with packing material to keep their device safe during shipping. There will be three different box sizes for the phones, tablets, and laptops. All of the box sizes are the same style of box. We are in need of a sleek, modern, and appealing design on the box with packing directions on the inside lid of the box. We want the packing instructions to be simple and easy to understand. Maybe there could be a picture along with each step, but this is not required. Our company wants to be seen as making fast payments to customers, trustworthy and having an easy process. Be creative, we are open to anything! Any creative writing you think that would be beneficial is welcome.

Box Information:

1. All of our boxes are white
2. Small Box 9x5x1.5 inches
3. Medium Box 13x11x2 inches
4. Large Box 18x10x3 inches
5. On the inside of the box, there will foam on the bottom and around the sides so no design is required there.

Other Information:

1. We have included an attachment that shows what the box will look like but please use your own mockup or box picture as you wish to show us the designs better.
2. Our website is currently undergoing a massive revamp and being is being completely redone. The current website we have will be of no use as our entire business model is changing as well.
3. Please contact us with any questions!

Target Market(s)

People trying to get cash for their old gadgets.

Font styles to use
Other font styles liked:
• Montserrat

Requirements
Must have
• Things to include on the box:
• 1. Our Website: BrightRelayHQ.com
• 2. Our logo (please use the logo with the BR above our name)
• 3. Packing instructions on the inside lid of the box (directions are attached)
• 4. There will be a shipping label on the top of the box so make sure no important information is towards the middle (logo ect.). The shipping label will take up most of the top of the box on the smallest box and will never be seen so keep that in mind.
• 5. The words "FAST, EASY, & TRUSTED" on the outside of the box
• 6. Social media icons (Facebook, Twitter, and Instagram)
• 7. The box must stay white
• 8. Our colors are attached in File 1
Nice to have
• 1. Mockup pictures showing a visual image along with each step for the packing instructions. For example, a visual of putting the phone in between the foam, putting the label on the box, putting the sticker on the box to seal it etc.
Should not have
• 1. Should not just be our logo, name, and website on the box. We could have created a design like this on our own without spending any money. Please keep this in mind when creating a design for us. We want something creative and original.
• 2. Should not change the colors of our logo. The logo colors must stay as is.

```html
<!DOCTYPE html>
<html lang="en">
<head>
<meta charset="utf-8">
<title>BrightRelayHQ Shipping Box Dieline</title>
<link rel="stylesheet" href="https://fonts.googleapis.com/css2?family=Montserrat:ital,wght@0,400;0,500;0,600;0,700;1,800&display=swap">
<style>
  :root {
    --navy: #072b5a;
    --orange: #fd4a05;
    --cyan: #37bcd3;
    --white: #ffffff;
    --dots: #ececec;
    --label-edge: #d6d6d6;
    --muted: #9a9a9a;
    --ink: #1d1d1d;
  }
  html, body {
    margin: 0;
    padding: 0;
    width: 1200px;
    height: 1150px;
    overflow: hidden;
    background: var(--white);
  }
  .dieline {
    display: block;
    width: 1200px;
    height: 1150px;
    font-family: "Montserrat", sans-serif;
  }
  .fill-navy { fill: var(--navy); }
  .fill-orange { fill: var(--orange); }
  .fill-cyan { fill: var(--cyan); }
  .panel-white { fill: var(--white); stroke: #222; stroke-width: 1; }
  .slot { fill: none; stroke: #222; stroke-width: 1; }
  .dot-field { fill: var(--dots); }
  .label-zone { fill: var(--white); stroke: var(--label-edge); stroke-width: 3; }
  .label-hint { fill: var(--muted); font-size: 14px; font-family: Arial, Helvetica, sans-serif; }
  .instructions { fill: var(--ink); font-size: 12px; font-family: Arial, Helvetica, sans-serif; }
  .social-mark { fill: #1a3fe0; }
  .social-name { fill: var(--navy); font-size: 13px; font-weight: 500; }
  .brand-name { fill: var(--navy); font-size: 37px; font-weight: 500; }
  .tagline { fill: var(--white); font-size: 41px; font-weight: 800; font-style: italic; }
</style>
</head>
<body>
<svg class="dieline" viewBox="0 0 1500 1438" xmlns="http://www.w3.org/2000/svg">
  <!-- lid top flap -->
  <polygon class="fill-orange" points="143,0 1357,0 1357,123 1320,123 1196,148 303,148 180,123 143,123"/>

  <!-- lid side flaps -->
  <g class="lid-side-left">
    <rect class="fill-navy" x="6" y="148" width="149" height="496"/>
    <rect class="fill-navy" x="0" y="248" width="8" height="99"/>
    <rect class="fill-navy" x="0" y="446" width="8" height="99"/>
    <rect class="fill-orange" x="155" y="148" width="148" height="496"/>
  </g>
  <g class="lid-side-right">
    <rect class="fill-orange" x="1196" y="148" width="149" height="496"/>
    <rect class="fill-navy" x="1345" y="148" width="149" height="496"/>
    <rect class="fill-navy" x="1492" y="248" width="8" height="99"/>
    <rect class="fill-navy" x="1492" y="446" width="8" height="99"/>
  </g>

  <!-- lid panel -->
  <rect class="panel-white" x="303" y="148" width="893" height="496"/>
  <path class="slot" d="M303,248 H310 V347 H303 M303,446 H310 V545 H303 M1196,248 H1189 V347 H1196 M1196,446 H1189 V545 H1196"/>

  <!-- dust flaps -->
  <polygon class="fill-orange" points="143,670 180,670 303,645 303,793 143,793"/>
  <polygon class="fill-orange" points="1357,670 1320,670 1196,645 1196,793 1357,793"/>

  <!-- side walls -->
  <path class="fill-navy" d="M303,793 L205,805 Q155,812 155,862 L155,1225 Q155,1270 205,1277 L303,1289 Z"/>
  <path class="fill-navy" d="M1196,793 L1294,805 Q1345,812 1345,862 L1345,1225 Q1345,1270 1294,1277 L1196,1289 Z"/>

  <!-- front panel -->
  <rect x="303" y="644" width="893" height="645" fill="var(--white)"/>
  <polygon class="dot-field" role="img" aria-label="Light grey dot pattern background" points="697,795 1196,795 1196,1289 622,1289"/>

  <!-- bottom flap -->
  <rect class="fill-navy" x="155" y="1289" width="1190" height="149" rx="62" ry="62"/>

  <!-- diagonal brand stripes -->
  <polygon class="fill-navy" points="557,644 596,644 475,1438 436,1438"/>
  <polygon class="fill-orange" points="596,644 652,644 531,1438 475,1438"/>
  <polygon class="fill-cyan" points="652,644 720,644 600,1438 531,1438"/>

  <!-- packing instructions (read from the lid side) -->
  <g class="instructions">
    <text x="1180" y="749" transform="rotate(180 1180 749)">Packing Instructions</text>
    <text x="1180" y="719" transform="rotate(180 1180 719)">1.Secure your device between the foam.</text>
    <text x="1180" y="704" transform="rotate(180 1180 704)">2.Seal the box with the adhesive strip and the enclosed sticker.</text>
    <text x="1180" y="688" transform="rotate(180 1180 688)">3.Place the prepaid shipping label on top of the label already on the box.</text>
    <text x="1180" y="673" transform="rotate(180 1180 673)">4.Drop the box off at your local shipping carrier or schedule a pickup.</text>
  </g>

  <!-- social handles -->
  <g class="social-row">
    <circle class="social-mark" cx="720" cy="822" r="11"/>
    <text class="social-name" x="736" y="826">BrightRelayHQ</text>
    <circle class="social-mark" cx="886" cy="822" r="11"/>
    <text class="social-name" x="902" y="826">BrightRelayHQ</text>
    <circle class="social-mark" cx="1051" cy="822" r="11"/>
    <text class="social-name" x="1067" y="826">BrightRelayHQ</text>
  </g>

  <!-- shipping label area -->
  <rect class="label-zone" x="685" y="1007" width="478" height="252" rx="40" ry="40"/>
  <text class="label-hint" x="924" y="1137" text-anchor="middle">Paste Shipping Lable Here</text>

  <!-- brand mark -->
  <g class="brand-lockup">
    <rect class="fill-navy" x="344" y="932" width="60" height="60"/>
    <text class="brand-name" x="449" y="1110" transform="rotate(-90 449 1110)" textLength="292" lengthAdjust="spacingAndGlyphs">BrightRelayHQ</text>
  </g>

  <!-- tagline -->
  <text class="tagline" x="647" y="1383" textLength="525" lengthAdjust="spacingAndGlyphs">FAST, EASY, &amp; TRUSTED</text>
</svg>
</body>
</html>
```